QuillNest - Home Income and Business Resources Platform

I am looking for a website template for a multi-purposed website. This website will feature:

1.) Website Directory with Ratings & comments on listings
2.) Company Blog
3.) Homepage with Content (see files for homepage mock)

I would like the Design to have a default width 1170px (wider then normal)

Of course I am looking for Pages for Listings to be designed.

Great looking BLOG Layout: http://journal.pagecrafter.example/html/blog.html

I would like 4 Versions of a Website Directory Listing "Box"
1.) Basic Listing Box
2.) Sponsored Listing Box
3.) Recommended Listing Box
4.) Stay Away From Listing Box

Information on the Listing Page (Like on a Category Page)
Site Name, Site URL, Website Image, # of Views, Rating and # of Comments

Information on the Listing Details Page:
Same as ABOVE + About website Description, Orvix Rank, Category Information

Decent looking examples is here: https://samples.kavlora.example/directory/computers/ and http://www.brimlisting.example/.

I will include some sketches and screenshots of things I like/looking for. As designers,you have creative freedom and are encouraged to show this. This is Phase one of this project and winning designer is guaranteed to have future work for this project.

Target Market(s)

Directory, business, websites

Industry/Entity Type

Business

Coding

Number of Pages Required

5+ page

Font styles to use
Sans Serif

Colors

Designer to choose colors to be used in the design.

Requirements
Must have
• Professional yet clean look. The use of Icons & images
• Unique Look
Should not have
• Any exact copies of any examples I provided

```html
<!DOCTYPE html>
<html lang="en">
<head>
<meta charset="utf-8">
<title>QuillNest – Home Income &amp; Business Resources</title>
<link rel="stylesheet" href="https://fonts.googleapis.com/css2?family=Lato:wght@400;700;900&family=Open+Sans:wght@400;600&display=swap">
<style>
  :root{
    --orange:#f0892c;
    --ink:#2b2b2b;
    --body:#666;
    --page:#f3f3f3;
    --card:#ffffff;
    --line:#dedede;
    --footer:#222222;
  }
  *{box-sizing:border-box;margin:0;padding:0}
  html,body{width:1200px;height:951px;overflow:hidden}
  body{position:relative;background:var(--page);font-family:"Open Sans",Arial,sans-serif;color:var(--body)}
  .abs{position:absolute}

  /* header */
  .site-header{left:0;top:0;width:1200px;height:81px;background:#fff;border-top:3px solid var(--orange);box-shadow:0 1px 3px rgba(0,0,0,.12)}
  .brand{left:97px;top:28px;font:900 23px/1 Lato,Arial,sans-serif;color:var(--ink);letter-spacing:.3px}
  .main-nav a{position:absolute;top:36px;font:700 14.5px/1 Lato,Arial,sans-serif;color:var(--ink);text-decoration:none}
  .main-nav a.active{color:var(--orange)}
  .search-icon{left:987px;top:37px}
  .login-btn{left:1021px;top:27px;width:80px;height:35px;border:1px solid #bbb;display:flex;align-items:center;justify-content:center;gap:6px;font:700 14.5px/1 Lato,Arial,sans-serif;color:var(--orange)}

  /* about */
  .about{left:99px;top:166px;width:758px;height:245px;background:#fff;border:3px solid #fff;box-shadow:0 0 3px rgba(0,0,0,.15);overflow:hidden}
  .about-photo{left:0;top:0;width:480px;height:100%;background:linear-gradient(90deg,#c9a48f 0%,#d8c3bb 35%,#ebe4e2 65%,#ffffff 100%)}
  .about-title{left:330px;top:26px;font:700 21px/1 Lato,Arial,sans-serif;color:var(--ink)}
  .about-sub{left:330px;top:58px;font:400 15.5px/1 Lato,Arial,sans-serif;color:var(--orange)}
  .about-text{left:330px;top:84px;width:400px;font-size:12.6px;line-height:22.3px}
  .btn{display:flex;align-items:center;justify-content:center;border:1px solid #bbb;background:#fff;font:700 12.5px/1 Lato,Arial,sans-serif;color:var(--orange);letter-spacing:.3px}
  .about .btn{left:330px;top:184px;width:94px;height:32px}

  /* feature cards */
  .card{top:441px;width:237px;height:348px;background:var(--card);box-shadow:0 0 3px rgba(0,0,0,.12)}
  .card-photo{left:3px;top:3px;width:231px;height:137px}
  .card-icon{left:84px;top:104px;width:69px;height:69px;border-radius:50%;background:var(--orange);border:3px solid #fff;display:flex;align-items:center;justify-content:center}
  .card-title{left:0;top:182px;width:100%;text-align:center;font:400 18px/27px Lato,Arial,sans-serif;color:var(--ink)}
  .card-text{left:8px;top:244px;width:221px;text-align:center;font-size:12.5px;line-height:23px}
  .card .btn{left:67px;top:333px;width:103px;height:31px}

  /* sidebar */
  .sponsored{left:887px;top:166px;width:214px;height:389px;background:#fff;border:1px solid var(--line)}
  .sponsored-head{left:-1px;top:-1px;width:214px;height:50px;background:var(--orange);color:#fff;font:700 20px/50px Lato,Arial,sans-serif;padding-left:21px}
  .badge{width:91px;height:54px;border:1px solid var(--line);background:#fff;display:flex;align-items:center;justify-content:center}
  .badge span{display:block;width:58px;height:16px;border-radius:3px;background:#d6d6d6}
  .promo{left:887px;top:590px;width:214px;height:216px;background:#fff;border:3px solid #fff;box-shadow:0 0 3px rgba(0,0,0,.15)}
  .promo-art{left:0;top:0;width:100%;height:100%;background:linear-gradient(180deg,#efe9dc 0%,#e7dcc6 70%,#b8742e 88%,#8a4a1d 100%)}

  .site-footer{left:0;top:884px;width:1200px;height:67px;background:var(--footer);color:#eee;text-align:center;font-size:12.5px;line-height:67px}
</style>
</head>
<body>

<header class="abs site-header">
  <div class="abs brand">QuillNest</div>
  <nav class="main-nav">
    <a class="active" style="left:330px" href="#">HOME</a>
    <a style="left:406px" href="#">ABOUT US</a>
    <a style="left:511px" href="#">RESOURCES</a>
    <a style="left:626px" href="#">BUSINESS DIRECTORY</a>
    <a style="left:812px" href="#">NEWS</a>
    <a style="left:886px" href="#">CONTACT</a>
  </nav>
  <svg class="abs search-icon" width="15" height="15" viewBox="0 0 16 16" aria-label="Search"><circle cx="6.5" cy="6.5" r="5" fill="none" stroke="#2b2b2b" stroke-width="2.2"/><line x1="10.3" y1="10.3" x2="15" y2="15" stroke="#2b2b2b" stroke-width="2.4" stroke-linecap="round"/></svg>
  <div class="abs login-btn">
    <svg width="11" height="13" viewBox="0 0 11 13"><path d="M2.5 6V4a3 3 0 0 1 6 0v2" fill="none" stroke="#f0892c" stroke-width="1.8"/><rect x="0.5" y="6" width="10" height="7" rx="1" fill="#f0892c"/></svg>
    LOGIN
  </div>
</header>

<section class="abs about">
  <div class="abs about-photo" role="img" aria-label="Smiling couple looking at a laptop together"></div>
  <h1 class="abs about-title">ABOUT QUILLNEST</h1>
  <p class="abs about-sub">We are Home Income &amp; Business resources directory.</p>
  <p class="abs about-text">At vero eos et accusamus et iusto odio dignissimos ducimus qui bland itiis praesentium voluptatum deleniti atque corrupti quos dolores etqu as molestias excepturi sint occaecati cupiditate non provident, simique sunt in culpa qui officia deserunt moll.</p>
  <a class="abs btn">READ MORE</a>
</section>

<article class="abs card" style="left:99px">
  <div class="abs card-photo" role="img" aria-label="Small house model, keys and fountain pen on documents" style="background:linear-gradient(135deg,#d9d3d3,#f1eeee 55%,#c9c7c8)"></div>
  <div class="abs card-icon"><svg width="32" height="30" viewBox="0 0 32 30"><path d="M16 2 1 15h4v13h8v-8h6v8h8V15h4z" fill="#fff"/></svg></div>
  <h2 class="abs card-title">Home Income<br>Resource Directory</h2>
  <p class="abs card-text">Find what you need, when you need it.The QuillNest website directory is your one-stop pit for anything</p>
  <a class="abs btn">READ MORE</a>
</article>

<article class="abs card" style="left:359px">
  <div class="abs card-photo" role="img" aria-label="Hands pointing at charts on a sunlit office desk" style="background:linear-gradient(135deg,#7a5a45,#e9d5b8 45%,#a88868)"></div>
  <div class="abs card-icon"><svg width="34" height="30" viewBox="0 0 34 30"><path d="M3 11h6l16-8v24L9 19H3z" fill="#fff"/><path d="M8 19l3 9h5l-3-9z" fill="#fff"/><path d="M28 10q4 5 0 10" fill="none" stroke="#fff" stroke-width="2.5"/></svg></div>
  <h2 class="abs card-title">Advertising<br>Benefits</h2>
  <p class="abs card-text">Everyone needs to advertise and we know just how to get your offer out to the right people. We have many</p>
  <a class="abs btn">READ MORE</a>
</article>

<article class="abs card" style="left:620px">
  <div class="abs card-photo" role="img" aria-label="Finger touching a glowing rising financial chart" style="background:linear-gradient(135deg,#3d5f8f,#8fb0d4 55%,#2e4c78)"></div>
  <div class="abs card-icon"><svg width="36" height="24" viewBox="0 0 36 24"><rect x="1.5" y="1.5" width="33" height="21" rx="2" fill="none" stroke="#fff" stroke-width="3"/><circle cx="18" cy="12" r="6" fill="#fff"/><rect x="5" y="5" width="4" height="3" fill="#fff"/><rect x="27" y="16" width="4" height="3" fill="#fff"/></svg></div>
  <h2 class="abs card-title">Earning With<br>QuillNest</h2>
  <p class="abs card-text">Join QuillNest and start earning money. When you share QuillNest and lock in an advertiser or premium listing,</p>
  <a class="abs btn">READ MORE</a>
</article>

<aside class="abs sponsored">
  <div class="abs sponsored-head">SPONSORED</div>
  <div class="abs badge" style="left:10px;top:75px"><span></span></div>
  <div class="abs badge" style="left:112px;top:75px"><span></span></div>
  <div class="abs badge" style="left:10px;top:152px"><span></span></div>
  <div class="abs badge" style="left:112px;top:152px"><span></span></div>
  <div class="abs badge" style="left:10px;top:229px"><span></span></div>
  <div class="abs badge" style="left:112px;top:229px"><span></span></div>
  <div class="abs badge" style="left:10px;top:306px"><span></span></div>
  <div class="abs badge" style="left:112px;top:306px"><span></span></div>
</aside>

<aside class="abs promo">
  <div class="abs promo-art" role="img" aria-label="Home equity advertisement with a house drawn from tools"></div>
</aside>

<footer class="abs site-footer">Copyright © 2017. QuillNest. All Rights Reserved.</footer>

</body>
</html>
```